Junk Removal Website Design

We are working with a Junk Removal company in California. They provide junk hauling services for commercial and residential throughout California.
Some sites to use for inspiration:
https://www.1877binclear.com
https://haulwaycleanoutpro.com
https://www.quarrybrawnmovingclutter.com
https://www.clutterliftwardens.com
Thank you for taking the time to consider designing a website for us. We are web developers based in Stockton, CA, USA. Most of our projects go through the same process. Understanding this process may help you win a project with us. We custom-code all of our websites in-house. We don’t have any requirements as to what tools you use for your design, but we ask that you follow these guidelines.
IMAGES:
If you use any images or icons in the design, we ask that you have a link to the asset so we can purchase the image/icon. Most of the designs we submit do not have the customer’s images on them unless they have some great images. Be creative; show us the feeling you are trying to portray with your image choices. Use any royalty-free site you choose. We subscribe to Vexaro and mainly use their images, but we can purchase images outside of Vexaro. PLEASE NOTE: we will not submit designs to clients with watermarks on the images.
FONTS:
We ask that you identify the fonts you’re using in the design. This can be done in a message if you want. We typically use Plimbet Fonts and Vexaro Fonts.
CONTENT:
We're always open to different content and ideas. We often submit designs with stock images so the client can see our vision. We typically take pictures after the website launch to use their images with our vision. Lorem Ipsum is fine for paragraphs, but we ask that you make the Headers with correct English. We want to be able to show the vision and identify the sections of the website.
INSPIRATION:
We typically add a couple of links in the brief of websites we like to help you get started in your design.
REVISIONS:
We do not often ask for revisions of the designs unless we see something in the design that may not appeal to the client. If there are slight changes that we want to make, we do that in the development process.
FEEDBACK:
We rarely give feedback on designs during the design process. We are working on many website projects and do not have the time to provide feedback. We usually respond if your request is well thought out and asks specific questions, but a note asking “feedback, please” usually goes unanswered.
Number of Pages Required
1 page

```html
<!DOCTYPE html>
<html lang="en">
<head>
<meta charset="utf-8">
<title>Clearload – Junk Removal</title>
<link href="https://fonts.googleapis.com/css2?family=Roboto:wght@400;500;700;900&display=swap" rel="stylesheet">
<style>
:root{
  --green:#4ba23c;
  --green-dark:#3d8a31;
  --ink:#222326;
  --text:#6b6e73;
  --nav:#2a2b2e;
  --footer:#2c2d31;
  --mint:#eef7ea;
  --white:#ffffff;
}
*{margin:0;padding:0;box-sizing:border-box}
html,body{width:1200px;height:4246px;overflow:hidden}
body{position:relative;font-family:'Roboto',sans-serif;color:var(--ink);background:var(--white)}
.abs{position:absolute}
.green{color:var(--green)}
.btn{position:absolute;background:var(--green);color:var(--white);font-weight:700;font-size:13px;display:flex;align-items:center;justify-content:center;text-transform:uppercase}
.btn::after{content:"";position:absolute;left:8px;top:8px;right:-8px;bottom:-8px;border:2px solid var(--ink)}
.btn.light::after{border-color:var(--white)}
.section-title{position:absolute;left:0;width:1200px;text-align:center;font-size:40px;font-weight:500;text-transform:uppercase;letter-spacing:-.5px}

/* header */
.logo{position:absolute;display:flex;align-items:center;gap:10px;font-weight:900;color:var(--green);text-transform:uppercase}
.logo .mark{border-radius:50%;background:var(--green)}
.social-dot{position:absolute;width:32px;height:32px;border:1.5px solid #9a9ca0;border-radius:50%}
.nav{position:absolute;left:0;top:102px;width:1200px;height:48px;background:var(--nav);z-index:1}
.nav a{position:absolute;top:17px;color:var(--white);font-size:13px;font-weight:700;text-decoration:none;text-transform:uppercase}
.nav a.active{color:var(--green)}
.nav .sep{position:absolute;top:15px;width:1px;height:18px;background:#555}
.call-block{position:absolute;left:0;top:0;z-index:2}
.call-item{z-index:3}

/* hero */
.hero-text{position:absolute;left:0;width:1200px;text-align:center;color:var(--white)}
.hero-arrow{position:absolute;width:22px;height:48px;background:var(--white)}

/* about */
.about p{position:absolute;left:110px;width:430px;font-size:14px;line-height:26px;color:var(--text);text-align:justify}

/* cards */
.card{position:absolute;background:var(--white);box-shadow:0 4px 14px rgba(0,0,0,.09)}
.card .photo{position:absolute;left:6px;top:6px;right:6px;height:202px}
.card .icon{position:absolute;left:50%;top:165px;width:84px;height:84px;margin-left:-42px;border-radius:50%;background:var(--green);border:5px solid #e9f4e5;display:flex;align-items:center;justify-content:center}
.card h3{position:absolute;left:0;right:0;top:270px;text-align:center;font-size:16px;font-weight:500;text-transform:uppercase}
.card p{position:absolute;left:20px;right:20px;top:305px;text-align:center;font-size:13.5px;line-height:24px;color:var(--text)}
.card .more{position:absolute;left:0;right:0;top:388px;text-align:center;font-size:13px;font-weight:700;color:var(--green)}
.round-arrow{position:absolute;width:34px;height:34px;border-radius:50%;display:flex;align-items:center;justify-content:center}

/* why */
.why-card{position:absolute;top:2390px;width:226px;height:253px;background:var(--white);box-shadow:0 5px 0 rgba(0,0,0,.25)}
.why-card .ring{position:absolute;left:69px;top:38px;width:88px;height:88px;border-radius:50%;border:2px solid #cfd1d3;display:flex;align-items:center;justify-content:center}
.why-card h3{position:absolute;left:0;right:0;top:152px;text-align:center;font-size:17px;font-weight:500;text-transform:uppercase}
.why-card p{position:absolute;left:15px;right:15px;top:184px;text-align:center;font-size:13.5px;line-height:22px;color:var(--text)}

/* testimonials */
.review .stars{position:absolute;left:24px;top:26px;color:#f0a21b;font-size:15px;letter-spacing:1px}
.review p{position:absolute;left:24px;right:24px;top:56px;font-size:13.5px;line-height:24px;color:#8b8d91}
.review .rule{position:absolute;left:24px;right:24px;top:168px;height:1px;background:#e2e3e5}
.review .avatar{position:absolute;left:24px;top:190px;width:56px;height:56px;border-radius:50%}
.review .name{position:absolute;left:100px;top:196px;font-size:15px;color:var(--green);font-weight:500}
.review .place{position:absolute;left:100px;top:224px;font-size:11.5px;color:#777}

/* contact */
.info-icon{position:absolute;width:66px;height:66px;border-radius:50%;background:var(--white);box-shadow:0 3px 12px rgba(0,0,0,.08);display:flex;align-items:center;justify-content:center}
.info-label{position:absolute;font-size:13px;font-weight:700;text-transform:uppercase}
.info-value{position:absolute;font-size:13px;line-height:21px;color:#555}
.field{position:absolute;background:var(--white);border:1px solid #e0e2e0;font-size:13.5px;color:#555;padding:0 18px;display:flex;align-items:center}
.field.area{align-items:flex-start;padding-top:15px}

/* footer */
.footer{position:absolute;left:0;top:3865px;width:1200px;height:381px;background:var(--footer);color:var(--white)}
.footer h4{position:absolute;font-size:16px;font-weight:700;text-transform:uppercase}
.footer .underline{position:absolute;height:3px;background:var(--green)}
.footer .f-icon{position:absolute;width:36px;height:36px;border-radius:50%;background:var(--white);display:flex;align-items:center;justify-content:center}
.footer .f-text{position:absolute;font-size:13.5px;line-height:23px}
.footer .link{position:absolute;font-size:13.5px}
</style>
</head>
<body>

<!-- HEADER -->
<header>
  <div class="logo" style="left:112px;top:28px;font-size:34px;line-height:34px;">
    <span class="mark" style="width:20px;height:20px"></span>CLEARLOAD
  </div>
  <div class="social-dot" style="left:478px;top:35px"></div>
  <div class="social-dot" style="left:518px;top:35px"></div>
  <div class="social-dot" style="left:558px;top:35px"></div>

  <div class="abs" style="left:624px;top:26px;width:54px;height:54px;border-radius:50%;box-shadow:0 2px 10px rgba(0,0,0,.12);display:flex;align-items:center;justify-content:center">
    <svg width="22" height="18" viewBox="0 0 22 18"><rect x="1" y="1" width="20" height="16" rx="2" fill="none" stroke="var(--green)" stroke-width="2"/><path d="M1 2l10 8 10-8" fill="none" stroke="var(--green)" stroke-width="2"/></svg>
  </div>
  <div class="abs" style="left:696px;top:33px;font-size:10px;color:#666">EMAIL US:</div>
  <div class="abs" style="left:696px;top:52px;font-size:14px;font-weight:500">info@clearload.com</div>

  <nav class="nav">
    <a class="active" style="left:110px">Home</a>
    <span class="sep" style="left:176px"></span>
    <a style="left:195px">Who We Are</a>
    <span class="sep" style="left:308px"></span>
    <a style="left:328px">What We Do</a>
    <span class="sep" style="left:440px"></span>
    <a style="left:460px">Pricing</a>
    <span class="sep" style="left:540px"></span>
    <a style="left:560px">Blog</a>
    <span class="sep" style="left:620px"></span>
    <a style="left:640px">Contact Us</a>
  </nav>

  <svg class="call-block" width="1200" height="150" viewBox="0 0 1200 150" aria-hidden="true">
    <polygon points="972,0 1200,0 1200,150 873,150" fill="var(--green)"/>
  </svg>
  <div class="abs call-item" style="left:1022px;top:33px;width:40px;height:40px;border-radius:50%;background:var(--ink);border:2px solid #fff;display:flex;align-items:center;justify-content:center">
    <svg width="16" height="16" viewBox="0 0 24 24"><path d="M6.6 10.8a15 15 0 006.6 6.6l2.2-2.2a1 1 0 011-.25 11.4 11.4 0 003.6.6 1 1 0 011 1V20a1 1 0 01-1 1A17 17 0 013 4a1 1 0 011-1h3.5a1 1 0 011 1 11.4 11.4 0 00.6 3.6 1 1 0 01-.25 1z" fill="#fff"/></svg>
  </div>
  <div class="abs call-item" style="left:1080px;top:48px;font-size:10px;font-weight:700;color:#fff">CALL US TODAY!</div>
  <div class="abs call-item" style="left:951px;top:86px;font-size:26px;font-weight:500;color:#fff;white-space:nowrap">+1 (555) 014 2290</div>
</header>

<!-- HERO -->
<section>
  <svg class="abs" style="left:0;top:150px" width="1200" height="690" viewBox="0 0 1200 690">
    <defs>
      <linearGradient id="heroPhoto" x1="0" y1="0" x2="1" y2="1">
        <stop offset="0" stop-color="#5f6e66"/>
        <stop offset=".45" stop-color="#2f5a8c"/>
        <stop offset=".8" stop-color="#4a6a3c"/>
        <stop offset="1" stop-color="#7d8e55"/>
      </linearGradient>
    </defs>
    <polygon role="img" aria-label="Blue dumpster filled with debris and yard waste on a residential street" points="0,0 1200,0 1200,520 0,670" fill="url(#heroPhoto)"/>
    <polygon points="0,0 1200,0 1200,520 0,670" fill="rgba(0,0,0,.22)"/>
    <polygon points="110,660 1200,520 1200,548 110,686" fill="var(--green)"/>
  </svg>
  <div class="hero-text" style="top:356px;font-size:42px;font-weight:500">JUNK REMOVAL</div>
  <div class="hero-text" style="top:422px;font-size:19px;line-height:30px">Lorem ipsum dolor sit amet, consectetur adipiscing<br>elit, sed do eiusmod incut laborea.</div>
  <div class="btn light" style="left:532px;top:508px;width:128px;height:46px">Get Started</div>
  <div class="hero-arrow" style="left:0;top:402px;border-radius:0 24px 24px 0"><svg width="22" height="48" viewBox="0 0 22 48"><path d="M13 18l-6 6 6 6" fill="none" stroke="var(--green)" stroke-width="2.5"/></svg></div>
  <div class="hero-arrow" style="left:1178px;top:402px;border-radius:24px 0 0 24px"><svg width="22" height="48" viewBox="0 0 22 48"><path d="M9 18l6 6-6 6" fill="none" stroke="var(--green)" stroke-width="2.5"/></svg></div>
</section>

<!-- ABOUT -->
<section class="about">
  <h2 class="abs" style="left:110px;top:966px;font-size:42px;font-weight:500">ABOUT <span class="green">US</span></h2>
  <p style="top:1042px">Lorem ipsum dolor sit amet, consectetur adipiscing elit, sed do eiusmod tempor incididunt ut labore et dolore magna aliqua. Ut enim ad minim veniam, quis nostrud exercitation ullamco laboris nisi ut aliquidunt ut laboripea.</p>
  <p style="top:1160px">Sed um dolor sit amet, consectetur adipiscing elit, sed do eiusmod tempor incididunt ut labore et dolore magna aliqua. Ut enim ad minim veniam, quis nostrud exercitation.</p>
  <div class="btn" style="left:110px;top:1271px;width:134px;height:50px">Learn More</div>

  <svg class="abs" style="left:720px;top:1040px" width="372" height="326" viewBox="0 0 372 326" aria-hidden="true">
    <path d="M302 4 H364 V318 H16 V256" fill="none" stroke="var(--ink)" stroke-width="8"/>
  </svg>
  <div role="img" aria-label="Worker wheeling a garbage bin past a leafy hedge" class="abs" style="left:715px;top:885px;width:297px;height:335px;background:linear-gradient(160deg,#6d8b3d,#b8c0a6 55%,#7a8a9a)"></div>
  <div role="img" aria-label="Dumpster loaded with discarded wooden boards" class="abs" style="left:626px;top:1055px;width:223px;height:247px;background:linear-gradient(180deg,#b98a55,#8a5c34 60%,#2d5ea8 72%,#2450a0);border:6px solid #fff;box-sizing:content-box;margin:-6px 0 0 -6px"></div>
</section>

<!-- SERVICES -->
<section>
  <div class="abs" style="left:0;top:1492px;width:1200px;height:741px;background:var(--mint)"></div>
  <h2 class="section-title" style="top:1558px"><span class="green">OUR</span> SERVICES</h2>
  <div class="btn" style="left:384px;top:1638px;width:201px;height:48px;background:#fff;color:var(--ink);box-shadow:0 2px 8px rgba(0,0,0,.06);font-weight:500;font-size:12.5px">Commercial Services</div>
  <div class="btn" style="left:606px;top:1638px;width:201px;height:48px;font-weight:500;font-size:12.5px">Residential Services</div>

  <div class="card" style="left:110px;top:1739px;width:307px;height:420px">
    <div class="photo" role="img" aria-label="Old furniture piled in a driveway for clean-out" style="background:linear-gradient(180deg,#6f8a5a,#a39480 60%,#76705f)"></div>
    <div class="icon"><svg width="36" height="36" viewBox="0 0 36 36" fill="none" stroke="#fff" stroke-width="2"><path d="M24 4l-8 14"/><path d="M10 18h14l2 14H8z"/><path d="M13 24v8M18 24v8M22 24v8"/></svg></div>
    <h3>Clean Outs</h3>
    <p>Lorem ipsum dolor sit amet, consectetur adipiscing elit, sed do eiusmod tempor incididunt ut laborea.</p>
    <div class="more">READ MORE &#10140;</div>
  </div>
  <div class="card" style="left:447px;top:1739px;width:307px;height:420px">
    <div class="photo" role="img" aria-label="Movers unloading boxes and a sofa from a van" style="background:linear-gradient(180deg,#d8d4cc,#c7a57a 60%,#8a6a45)"></div>
    <div class="icon"><svg width="36" height="36" viewBox="0 0 36 36" fill="none" stroke="#fff" stroke-width="2"><rect x="8" y="16" width="20" height="10"/><path d="M6 14v14M30 14v14M10 26v4M26 26v4M12 16v-6h12v6"/></svg></div>
    <h3>Furniture Removal</h3>
    <p>Lorem ipsum dolor sit amet, consectetur adipiscing elit, sed do eiusmod tempor incididunt ut laborea.</p>
    <div class="more">READ MORE &#10140;</div>
  </div>
  <div class="card" style="left:783px;top:1739px;width:307px;height:420px">
    <div class="photo" role="img" aria-label="Blue roll-off container full of yard waste" style="background:linear-gradient(180deg,#8fa86b,#2f6cb6 50%,#7a7d7a)"></div>
    <div class="icon"><svg width="36" height="36" viewBox="0 0 36 36" fill="none" stroke="#fff" stroke-width="2"><path d="M6 30h24M9 30V18M15 30V14M21 30V16M27 30V20"/><circle cx="12" cy="9" r="3"/><circle cx="24" cy="9" r="3"/></svg></div>
    <h3>Yard Waste Removal</h3>
    <p>Lorem ipsum dolor sit amet, consectetur adipiscing elit, sed do eiusmod tempor incididunt ut laborea.</p>
    <div class="more">READ MORE &#10140;</div>
  </div>

  <div class="round-arrow" style="left:44px;top:1931px;background:#fff;box-shadow:0 2px 6px rgba(0,0,0,.1)"><svg width="12" height="12" viewBox="0 0 12 12"><path d="M8 2L4 6l4 4" fill="none" stroke="var(--ink)" stroke-width="2"/></svg></div>
  <div class="round-arrow" style="left:1120px;top:1931px;background:var(--green)"><svg width="12" height="12" viewBox="0 0 12 12"><path d="M4 2l4 4-4 4" fill="none" stroke="#fff" stroke-width="2"/></svg></div>
</section>

<!-- WHY CHOOSE US -->
<section>
  <div role="img" aria-label="Green-tinted photo of a junk removal crew at work" class="abs" style="left:0;top:2233px;width:1200px;height:491px;background:linear-gradient(135deg,#58ab48,#3f9136 50%,#4c9e3f)"></div>
  <h2 class="section-title" style="top:2300px;color:#fff">WHY CHOOSE US</h2>
  <div class="why-card" style="left:110px">
    <div class="ring"><svg width="40" height="40" viewBox="0 0 40 40" fill="none" stroke="var(--ink)" stroke-width="2"><path d="M6 18a14 11 0 1 1 6 9l-6 5 2-7"/><path d="M13 15h14M13 20h10"/></svg></div>
    <h3>Free Quotes</h3><p>Lorem ipsum dolor sit amet, consectetur adipi.</p>
  </div>
  <div class="why-card" style="left:363px">
    <div class="ring"><svg width="40" height="40" viewBox="0 0 40 40" fill="none" stroke="var(--ink)" stroke-width="2"><circle cx="20" cy="14" r="7"/><path d="M6 28c6-4 10 2 16 0l8-4M4 34h10l10-2"/></svg></div>
    <h3>Full Service</h3><p>Lorem ipsum dolor sit amet, consectetur adipi.</p>
  </div>
  <div class="why-card" style="left:613px">
    <div class="ring"><svg width="40" height="40" viewBox="0 0 40 40" fill="none" stroke="var(--ink)" stroke-width="2"><rect x="14" y="6" width="20" height="28"/><path d="M19 13h10M19 19h10M19 25h10"/><circle cx="10" cy="20" r="5"/><path d="M7 24l-1 9 4-2 4 2-1-9"/></svg></div>
    <h3>Licensed &amp; Insured</h3><p>Lorem ipsum dolor sit amet, consectetur adipi.</p>
  </div>
  <div class="why-card" style="left:864px">
    <div class="ring"><svg width="40" height="40" viewBox="0 0 40 40" fill="none" stroke="var(--ink)" stroke-width="2"><path d="M12 34V22h4l4-8c2 0 3 1 3 3l-1 5h8l-2 12z"/><path d="M8 12l2-4 2 4M18 8l2-4 2 4M28 12l2-4 2 4"/></svg></div>
    <h3>5 Star Rating</h3><p>Lorem ipsum dolor sit amet, consectetur adipi.</p>
  </div>
</section>

<!-- TESTIMONIALS -->
<section>
  <h2 class="section-title" style="top:2835px"><span class="green">WHAT OUR</span> CLIENTS SAY</h2>
  <div class="card review" style="left:110px;top:2930px;width:307px;height:275px">
    <div class="stars">★★★★★</div>
    <p>Lorem ipsum dolor sit amet, consectetur adipiscing elit, sed do eiusmod tempor incididunt ut labore et dolore magna ali qu nim ad minim veniam.</p>
    <div class="rule"></div>
    <div class="avatar" role="img" aria-label="Client portrait" style="background:linear-gradient(135deg,#9bb1c6,#5c7390)"></div>
    <div class="name">John Smith</div><div class="place">California, United States</div>
  </div>
  <div class="card review" style="left:447px;top:2930px;width:307px;height:275px">
    <div class="stars">★★★★★</div>
    <p>Lorem ipsum dolor sit amet, consectetur adipiscing elit, sed do eiusmod tempor incididunt ut labore et dolore magna ali qu nim ad minim veniam.</p>
    <div class="rule"></div>
    <div class="avatar" role="img" aria-label="Client portrait" style="background:linear-gradient(135deg,#8a6a55,#3d2c24)"></div>
    <div class="name">John Smith</div><div class="place">California, United States</div>
  </div>
  <div class="card review" style="left:783px;top:2930px;width:307px;height:275px">
    <div class="stars">★★★★★</div>
    <p>Lorem ipsum dolor sit amet, consectetur adipiscing elit, sed do eiusmod tempor incididunt ut labore et dolore magna ali qu nim ad minim veniam.</p>
    <div class="rule"></div>
    <div class="avatar" role="img" aria-label="Client portrait" style="background:linear-gradient(135deg,#c9b9a3,#6d5a48)"></div>
    <div class="name">John Smith</div><div class="place">California, United States</div>
  </div>
  <div class="round-arrow" style="left:34px;top:3050px;background:var(--mint)"><svg width="12" height="12" viewBox="0 0 12 12"><path d="M8 2L4 6l4 4" fill="none" stroke="var(--ink)" stroke-width="2"/></svg></div>
  <div class="round-arrow" style="left:1130px;top:3050px;background:var(--green)"><svg width="12" height="12" viewBox="0 0 12 12"><path d="M4 2l4 4-4 4" fill="none" stroke="#fff" stroke-width="2"/></svg></div>
</section>

<!-- CONTACT -->
<section>
  <div class="abs" style="left:0;top:3322px;width:1200px;height:543px;background:var(--mint)"></div>
  <h2 class="section-title" style="top:3382px"><span class="green">GET IN</span> TOUCH</h2>

  <div class="info-icon" style="left:204px;top:3461px"><svg width="22" height="26" viewBox="0 0 22 26"><path d="M11 2a8 8 0 018 8c0 6-8 14-8 14S3 16 3 10a8 8 0 018-8z" fill="none" stroke="var(--green)" stroke-width="2"/><circle cx="11" cy="10" r="3" fill="var(--green)"/></svg></div>
  <div class="info-label" style="left:298px;top:3464px">Location:</div>
  <div class="info-value" style="left:297px;top:3488px">712, Quarry Lane Delta Road,<br>United States</div>

  <div class="info-icon" style="left:512px;top:3461px"><svg width="22" height="22" viewBox="0 0 24 24"><path d="M6.6 10.8a15 15 0 006.6 6.6l2.2-2.2a1 1 0 011-.25 11.4 11.4 0 003.6.6 1 1 0 011 1V20a1 1 0 01-1 1A17 17 0 013 4a1 1 0 011-1h3.5a1 1 0 011 1 11.4 11.4 0 00.6 3.6 1 1 0 01-.25 1z" fill="none" stroke="var(--green)" stroke-width="2"/></svg></div>
  <div class="info-label" style="left:607px;top:3474px">Phone:</div>
  <div class="info-value" style="left:604px;top:3498px">+1 (555) 014 2290</div>

  <div class="info-icon" style="left:751px;top:3461px"><svg width="22" height="18" viewBox="0 0 22 18"><rect x="1" y="1" width="20" height="16" rx="2" fill="none" stroke="var(--green)" stroke-width="2"/><path d="M1 2l10 8 10-8" fill="none" stroke="var(--green)" stroke-width="2"/></svg></div>
  <div class="info-label" style="left:841px;top:3474px">Email:</div>
  <div class="info-value" style="left:841px;top:3498px">info@clearload.com</div>

  <div class="field" style="left:165px;top:3565px;width:283px;height:49px">Full Name</div>
  <div class="field" style="left:461px;top:3565px;width:281px;height:49px">Phone Number</div>
  <div class="field" style="left:752px;top:3565px;width:283px;height:49px">Email Address</div>
  <div class="field area" style="left:165px;top:3624px;width:870px;height:96px">Message</div>
  <div class="btn" style="left:512px;top:3738px;width:167px;height:50px">Send Message</div>
</section>

<!-- FOOTER -->
<footer class="footer">
  <div class="logo" style="left:110px;top:140px;font-size:40px;line-height:40px">
    <span class="mark" style="width:22px;height:22px"></span>CLEARLOAD
  </div>

  <h4 style="left:374px;top:54px">Contact Us</h4>
  <div class="underline" style="left:374px;top:84px;width:214px"></div>
  <div class="f-icon" style="left:374px;top:122px"><svg width="14" height="16" viewBox="0 0 22 26"><path d="M11 2a8 8 0 018 8c0 6-8 14-8 14S3 16 3 10a8 8 0 018-8z" fill="var(--green)"/></svg></div>
  <div class="f-text" style="left:429px;top:120px">712, Quarry Lane Delta Road,<br>United States</div>
  <div class="f-icon" style="left:374px;top:182px"><svg width="15" height="15" viewBox="0 0 24 24"><path d="M6.6 10.8a15 15 0 006.6 6.6l2.2-2.2a1 1 0 011-.25 11.4 11.4 0 003.6.6 1 1 0 011 1V20a1 1 0 01-1 1A17 17 0 013 4a1 1 0 011-1h3.5a1 1 0 011 1 11.4 11.4 0 00.6 3.6 1 1 0 01-.25 1z" fill="var(--green)"/></svg></div>
  <div class="f-text" style="left:429px;top:180px">Call Us:<br>+1 (555) 014 2290</div>
  <div class="f-icon" style="left:374px;top:242px"><svg width="15" height="12" viewBox="0 0 22 18"><rect x="1" y="1" width="20" height="16" rx="2" fill="var(--green)"/><path d="M1 2l10 8 10-8" fill="none" stroke="#fff" stroke-width="2"/></svg></div>
  <div class="f-text" style="left:429px;top:240px">Email Us:<br>info@clearload.com</div>

  <h4 style="left:717px;top:54px">Quick Links</h4>
  <div class="underline" style="left:717px;top:84px;width:160px"></div>
  <div class="link" style="left:717px;top:118px">Home</div>
  <div class="link" style="left:717px;top:148px">Who We Are</div>
  <div class="link" style="left:717px;top:178px">What We Do</div>
  <div class="link" style="left:717px;top:208px">Pricing</div>
  <div class="link" style="left:717px;top:238px">Blog</div>
  <div class="link" style="left:717px;top:268px">Contact Us</div>

  <h4 style="left:949px;top:54px">Follow Us</h4>
  <div class="underline" style="left:949px;top:84px;width:115px"></div>
  <div class="f-icon" style="left:949px;top:122px"></div>
  <div class="f-text" style="left:1004px;top:120px">Follow Us On<br>FRIENDWALL</div>
  <div class="f-icon" style="left:949px;top:182px"></div>
  <div class="f-text" style="left:1004px;top:180px">Follow Us On<br>SNAPGRID</div>
  <div class="f-icon" style="left:949px;top:242px"></div>
  <div class="f-text" style="left:1004px;top:240px">Follow Us On<br>CHIRPLINE</div>

  <div class="abs" style="left:0;top:313px;width:1200px;height:1px;background:#45464a"></div>
  <div class="abs" style="left:0;top:333px;width:1200px;text-align:center;font-size:13px">Copyright © 2023 CLEARLOAD - All Rights Reserved.</div>
</footer>

</body>
</html>
```